Banner for promote service of debit card

We are PagaVelo and we need the banners to be posted on the facebook and instagram pages.
We want something to communicate that it is an exclusive debit card full of services.
Low commissions.
Our competitors:
https://www.nortapay-pagos.it/it/home.html
https://www.zelkor-conti.it/it/
https://www.fotoreelz.it/serravanbank/
sendquillo
maybe some banner that makes the idea of a convenient debit card that everyone can use.
Girls enjoying card shopping.
Please check also website for slogans and phrases to use
https://www.pagavelo-carta.it/
Should show the services.
We must convey that it is a fast, simple card that guarantees privacy.
We need strong banners that attract people as these ban will be sponsored on instagram and facebook
Target Market(s)
People 18-35 y
Open Bank account. low commissions. Easy to use. No limits. 100% Privacy.
Requirements
Must have
- Written in Italian.

```html
<!DOCTYPE html>
<html lang="it">
<head>
<meta charset="UTF-8">
<title>PagaVelo – Una carta per tutti</title>
<link rel="stylesheet" href="https://fonts.googleapis.com/css2?family=Raleway:wght@400;500;600;700;800&display=swap">
<style>
  :root {
    --ink: #1f1f1f;
    --magenta: #d4166a;
    --magenta-band: #d3176a;
    --sun: #fbb613;
    --paper: #ffffff;
    --mist: #eaf1f6;
    --logo-grey: #6c6c6c;
    --font-main: "Raleway", Arial, sans-serif;
  }
  * { margin: 0; padding: 0; box-sizing: border-box; }
  html, body { width: 1200px; height: 1200px; overflow: hidden; }
  body { font-family: var(--font-main); background: var(--paper); }

  .banner {
    position: relative;
    width: 1200px;
    height: 1200px;
    overflow: hidden;
    background: linear-gradient(100deg, #ffffff 0%, #ffffff 40%, var(--mist) 100%);
  }

  .hero-photo {
    position: absolute;
    left: 520px;
    top: 0;
    width: 680px;
    height: 930px;
    background:
      radial-gradient(ellipse 30% 22% at 46% 38%, #e8b9a4 0%, rgba(232,185,164,0) 100%),
      radial-gradient(ellipse 55% 45% at 45% 35%, #8a4a2e 0%, rgba(138,74,46,0) 100%),
      radial-gradient(ellipse 50% 30% at 60% 85%, #4a1a22 0%, rgba(74,26,34,0) 100%),
      linear-gradient(90deg, rgba(255,255,255,0) 0%, #dde9f1 30%, #cfe0ec 100%);
  }

  .shapes { position: absolute; inset: 0; }

  .card-stack { position: absolute; left: 0; top: 0; width: 1200px; height: 1200px; }

  .headline {
    position: absolute;
    left: 108px;
    top: 92px;
    font-weight: 800;
    font-size: 83px;
    line-height: 74px;
    letter-spacing: -0.5px;
    text-transform: uppercase;
  }
  .headline .lead { color: var(--ink); display: block; }
  .headline .accent { color: var(--magenta); display: block; }

  .tagline {
    position: absolute;
    left: 111px;
    top: 352px;
    font-size: 24px;
    font-weight: 400;
    color: #333;
  }

  .features {
    position: absolute;
    left: 108px;
    top: 462px;
    list-style: none;
  }
  .features li {
    position: relative;
    padding-left: 42px;
    font-size: 29px;
    font-weight: 600;
    color: var(--ink);
    line-height: 41.7px;
  }
  .features li::before {
    content: "";
    position: absolute;
    left: 2px;
    top: 11px;
    width: 21px;
    height: 21px;
    border: 3.5px solid var(--magenta);
    border-radius: 50%;
  }

  .brand {
    position: absolute;
    left: 890px;
    top: 1040px;
    display: flex;
    align-items: center;
    gap: 14px;
  }
  .brand-dot {
    width: 34px;
    height: 34px;
    border-radius: 50%;
    background: var(--magenta);
  }
  .brand-name {
    font-size: 40px;
    font-weight: 700;
    color: var(--logo-grey);
  }

  .contact {
    position: absolute;
    top: 1098px;
    display: flex;
    align-items: center;
    gap: 16px;
    color: var(--paper);
    font-size: 27px;
    font-weight: 700;
  }
  .contact.phone { left: 109px; }
  .contact.web { left: 426px; }
  .contact-icon {
    width: 48px;
    height: 48px;
    border-radius: 50%;
    background: var(--paper);
    display: flex;
    align-items: center;
    justify-content: center;
  }
</style>
</head>
<body>
<main class="banner">
  <div class="hero-photo" role="img" aria-label="Foto di una ragazza sorridente che porge una carta di debito"></div>

  <svg class="shapes" width="1200" height="1200" viewBox="0 0 1200 1200" aria-hidden="true">
    <polygon points="0,822 470,712 722,925 0,1000" fill="var(--sun)"/>
    <polygon points="0,1000 722,925 890,1200 0,1200" fill="var(--magenta-band)"/>
    <polygon points="722,925 1200,817 1200,1200 890,1200" fill="var(--paper)"/>
  </svg>

  <svg class="card-stack" width="1200" height="1200" viewBox="0 0 1200 1200" role="img" aria-label="Illustrazione di tre carte di debito colorate">
    <defs>
      <linearGradient id="cardGreen" x1="0" y1="0" x2="1" y2="1">
        <stop offset="0" stop-color="#2eb873"/><stop offset="1" stop-color="#3fe0c0"/>
      </linearGradient>
      <linearGradient id="cardBlue" x1="0" y1="0" x2="1" y2="1">
        <stop offset="0" stop-color="#0d5f8f"/><stop offset="1" stop-color="#25a9dc"/>
      </linearGradient>
      <linearGradient id="cardRed" x1="0" y1="0" x2="1" y2="1">
        <stop offset="0" stop-color="#d8a8c0"/><stop offset="1" stop-color="#e0303d"/>
      </linearGradient>
    </defs>
    <rect x="500" y="760" width="260" height="180" rx="14" fill="url(#cardGreen)" transform="rotate(-18 630 850)"/>
    <rect x="355" y="745" width="265" height="185" rx="14" fill="url(#cardBlue)" transform="rotate(-18 487 837)"/>
    <rect x="125" y="795" width="325" height="205" rx="16" fill="url(#cardRed)" transform="rotate(-18 287 897)"/>
  </svg>

  <h1 class="headline">
    <span class="lead">Tutto in uno!</span>
    <span class="accent">Una carta per</span>
    <span class="accent">tutti</span>
  </h1>

  <p class="tagline">Usalo come vuoi senza essere controllato</p>

  <ul class="features">
    <li>Apri un conto bancario.</li>
    <li>commissioni basse.</li>
    <li>Facile da usare.</li>
    <li>Senza limiti.</li>
    <li>Privacy al 100%.</li>
  </ul>

  <div class="brand">
    <span class="brand-dot"></span>
    <span class="brand-name">PagaVelo</span>
  </div>

  <div class="contact phone">
    <span class="contact-icon">
      <svg width="26" height="26" viewBox="0 0 24 24" aria-hidden="true">
        <path fill="var(--magenta)" d="M6.6 10.8a15.1 15.1 0 0 0 6.6 6.6l2.2-2.2c.3-.3.7-.4 1-.2 1.1.4 2.3.6 3.6.6.6 0 1 .4 1 1V20c0 .6-.4 1-1 1A17 17 0 0 1 3 4c0-.6.4-1 1-1h3.5c.6 0 1 .4 1 1 0 1.3.2 2.5.6 3.6.1.3 0 .7-.2 1z"/>
      </svg>
    </span>
    <span class="contact-text">800-246-8135</span>
  </div>

  <div class="contact web">
    <span class="contact-icon">
      <svg width="26" height="26" viewBox="0 0 24 24" aria-hidden="true">
        <g fill="none" stroke="var(--magenta)" stroke-width="2.6" stroke-linecap="round">
          <path d="M10 14a4 4 0 0 0 5.7 0l3.5-3.5a4 4 0 0 0-5.7-5.7l-1.2 1.2"/>
          <path d="M14 10a4 4 0 0 0-5.7 0l-3.5 3.5a4 4 0 0 0 5.7 5.7l1.2-1.2"/>
        </g>
      </svg>
    </span>
    <span class="contact-text">www.pagavelo-carta.it</span>
  </div>
</main>
</body>
</html>
```